Surgery Office Letterhead Design

I'm seeking new letterhead that will comprise all of our office locations and logo and other applicable information, per the following:

Office Locations:

Lakemont Institute for Jaw & Face Surgery at Cleburne
347 Hazelpine Court
Cleburne, Texas 76992
Phone 817.382.4706
Fax 817.382.9034

Lakemont Institute for Jaw & Face Surgery at Stephenville
518 Willowgate Boulevard
Stephenville, Texas 76998
Phone 254.563.2781
Fax 254.563.2789

Lakemont Institute for Jaw & Face Surgery at Belton
739 West 9th Avenue
Belton, Texas 76995
Phone 254.871.4035
Fax 254.871.4042

Other Info to include:

www.lakemontjawface.com
hello@lakemontjawface.com

Industry/Entity Type

Medical

Font styles to use
Serif
Sans Serif

Requirements
Must have
• See Project Description

```html
<!DOCTYPE html>
<html lang="en">
<head>
<meta charset="utf-8">
<title>Lakemont Institute for Jaw &amp; Face Surgery – Letterhead</title>
<link rel="stylesheet" href="https://fonts.googleapis.com/css2?family=Carlito:wght@400;700&family=Montserrat:wght@400;500;600&display=swap">
<style>
  :root {
    --backdrop: #d4d4d4;
    --paper: #ffffff;
    --navy: #1f3d6e;
    --navy-light: #7286a8;
    --ink: #1c1c1c;
    --body-ink: #2a2a2a;
    --sig-tone: #ececec;
  }
  * { margin: 0; padding: 0; box-sizing: border-box; }
  html, body { width: 1200px; height: 1200px; overflow: hidden; background: var(--backdrop); }
  .letterhead {
    position: absolute; left: 136px; top: 0;
    width: 927px; height: 1200px;
    background: var(--paper);
    font-family: "Carlito", "Calibri", sans-serif;
    color: var(--body-ink);
  }
  .brand {
    position: absolute; left: 560px; top: 82px;
    display: flex; align-items: center; gap: 12px;
    color: var(--navy); font-family: "Carlito", sans-serif; font-weight: 400;
  }
  .brand-dot { width: 46px; height: 46px; border-radius: 50%; background: var(--navy); }
  .brand-name { line-height: 1.05; text-transform: uppercase; }
  .brand-name .main { display: block; font-size: 31px; letter-spacing: 0.5px; }
  .brand-name .sub { display: block; font-size: 15.5px; letter-spacing: 0.4px; margin-top: 3px; }

  .office {
    position: absolute;
    font-family: "Montserrat", sans-serif;
    color: var(--ink);
    font-size: 12.4px; line-height: 15.5px;
  }
  .office h2 { font-size: 14px; font-weight: 500; color: var(--navy); line-height: 18px; margin-bottom: 6px; }
  .office address { font-style: normal; margin-bottom: 6px; }
  .office .line { display: flex; align-items: center; gap: 5px; line-height: 16.5px; }
  .office svg { width: 11px; height: 9px; fill: var(--navy); flex: none; }
  .office-cleburne { left: 45px; top: 223px; }
  .office-stephenville { left: 52px; top: 626px; }
  .office-belton { left: 59px; top: 1005px; }

  .letter { position: absolute; left: 253px; width: 600px; font-size: 17.8px; }
  h1.letter-title { top: 220px; font-size: 17.8px; font-weight: 700; color: #111; line-height: 22px; }
  p.letter { line-height: 32px; }
  .para-1 { top: 278px; }
  .para-2 { top: 565px; }
  .para-3 { top: 820px; }
  p.sign-off { top: 948px; line-height: 30px; }
  .signature { position: absolute; left: 263px; top: 996px; width: 150px; height: 52px; background: var(--sig-tone); border-radius: 4px; }
  p.signer-title { top: 1076px; line-height: 30px; }

  .footer-band {
    position: absolute; left: 0; bottom: 0; width: 927px; height: 52px;
    background: linear-gradient(90deg, var(--navy) 0%, #3b5684 45%, var(--navy-light) 100%);
    display: flex; align-items: center; padding-left: 270px; gap: 22px;
    font-family: "Montserrat", sans-serif; font-size: 12.5px; color: #fff;
  }
  .footer-band .contact { display: flex; align-items: center; gap: 9px; }
  .footer-band svg { width: 15px; height: 15px; fill: none; stroke: #fff; stroke-width: 1.5; }
</style>
</head>
<body>
<main class="letterhead">
  <header class="brand">
    <span class="brand-dot"></span>
    <span class="brand-name"><span class="main">Lakemont Institute</span><span class="sub">for Jaw &amp; Face Surgery</span></span>
  </header>

  <section class="office office-cleburne">
    <h2>Cleburne</h2>
    <address>347 Hazelpine Court<br>Cleburne, Texas 76992</address>
    <div class="line"><svg viewBox="0 0 12 10"><path d="M1 3.5C3 1 9 1 11 3.5L10 5 8 4V3H4v1L2 5z M3 6h6l1 3H2z"/></svg>817.382.4706</div>
    <div class="line"><svg viewBox="0 0 12 10"><path d="M1 3h2v7H1z M4 1h5v3H4z M4 5h7v5H4z"/></svg>817.382.9034</div>
  </section>

  <section class="office office-stephenville">
    <h2>Stephenville</h2>
    <address>518 Willowgate Boulevard<br>Stephenville, Texas 76998</address>
    <div class="line"><svg viewBox="0 0 12 10"><path d="M1 3.5C3 1 9 1 11 3.5L10 5 8 4V3H4v1L2 5z M3 6h6l1 3H2z"/></svg>254.563.2781</div>
    <div class="line"><svg viewBox="0 0 12 10"><path d="M1 3h2v7H1z M4 1h5v3H4z M4 5h7v5H4z"/></svg>254.563.2789</div>
  </section>

  <section class="office office-belton">
    <h2>Belton</h2>
    <address>739 West 9th Avenue<br>Belton, Texas 76995</address>
    <div class="line"><svg viewBox="0 0 12 10"><path d="M1 3.5C3 1 9 1 11 3.5L10 5 8 4V3H4v1L2 5z M3 6h6l1 3H2z"/></svg>254.871.4035</div>
    <div class="line"><svg viewBox="0 0 12 10"><path d="M1 3h2v7H1z M4 1h5v3H4z M4 5h7v5H4z"/></svg>254.871.4042</div>
  </section>

  <h1 class="letter letter-title">Lorem Ipsum is simply</h1>
  <p class="letter para-1">&nbsp;dummy text of the printing and typesetting industry. Lorem Ipsum has been the industry's standard dummy text ever since the 1500s, when an unknown printer took a galley of type and scrambled it to make a type specimen book. It has survived not only five centuries, but also the leap into electronic typesetting, remaining essentially unchanged. It was popularised in the 1960s with the release of Brightset sheets containing Lorem Ipsum passages, and more recently with desktop publishing software like Quillset Composer including versions of Lorem Ipsum.</p>
  <p class="letter para-2">It is a long established fact that a reader will be distracted by the readable content of a page when looking at its layout. The point of using Lorem Ipsum is that it has a more-or-less normal distribution of letters, as opposed to using 'Content here, content here.&nbsp; It is a long established fact that a reader will be distracted by the readable content of a page when looking at its layout. The point of using Lorem Ipsum is that it has a more-or-less normal distribution of letters, as opposed to using 'Content here, content here.</p>
  <p class="letter para-3">&nbsp;Contrary to popular belief, Lorem Ipsum is not simply random text. It has roots in a piece of classical Latin literature from 45 BC, making it over 2000 years old. Edwin Harrowgate, a Latin professor at Alderbrook College in Virginia,</p>
  <p class="letter sign-off">Lorem Ipsum</p>
  <div class="signature" role="img" aria-label="Handwritten signature"></div>
  <p class="letter signer-title">Lorem Ipsum is a dummy</p>

  <footer class="footer-band">
    <span class="contact"><svg viewBox="0 0 16 16"><rect x="1.5" y="4" width="13" height="9" rx="1"/><path d="M1.5 5l6.5 4.5L14.5 5"/></svg>hello@lakemontjawface.com</span>
    <span class="contact"><svg viewBox="0 0 16 16"><circle cx="8" cy="8" r="6.5"/><ellipse cx="8" cy="8" rx="3" ry="6.5"/><path d="M1.5 8h13M2.5 5h11M2.5 11h11"/></svg>www.lakemontjawface.com</span>
  </footer>
</main>
</body>
</html>
```